Fertility Book Cover

This is a book about infertility, treatment options and solutions. The book title is "No caminho do amanhecer". The book is in portuguese, but I believe that won't be a problem to design the cover. I need front and back covers design.
The author name, that should be in book is "Dra. Beatriz Morano Vasconti Telhado".

Letter case could be "No Caminho do Amanhecer"

This is the cover I created, but I don't like it: http://www.docuvelo.com/doc/583190462/27390518-cover

8.5" x 11"

Target Market(s)

Woman and Couples that desire kids and have problem about fertility

Colors
b768aa
e34196
6b449a

Requirements
Nice to have
• a link to our domain: www.ninhoclaro.org (not essential)
More happy images than sad woman...

```html
<!DOCTYPE html>
<html lang="pt-BR">
<head>
<meta charset="utf-8">
<title>No Caminho do Amanhecer</title>
<link href="https://fonts.googleapis.com/css2?family=Yellowtail&family=Mulish:wght@700;800&display=swap" rel="stylesheet">
<style>
  :root {
    --bg: #fde2f0;
    --plum: #6b449a;
    --orchid: #b768aa;
    --ornament: #d9b6dd;
    --photo-a: #f1ddd6;
    --photo-b: #d7c4bf;
  }
  html, body { margin: 0; padding: 0; overflow: hidden; }
  body { width: 927px; height: 1200px; background: var(--bg); }
  .cover { position: relative; width: 927px; height: 1200px; background: var(--bg); overflow: hidden; }
  .frame { position: absolute; inset: 0; }
  .corner-ornament { position: absolute; width: 130px; height: 130px; background: var(--ornament); opacity: .55; border-radius: 8px; }
  .corner-ornament.tl { left: 6px; top: 6px; }
  .corner-ornament.tr { right: 6px; top: 6px; }
  .corner-ornament.bl { left: 6px; bottom: 6px; }
  .corner-ornament.br { right: 6px; bottom: 6px; }
  .author {
    position: absolute; top: 82px; left: 0; width: 100%;
    text-align: center; margin: 0;
    font-family: "Yellowtail", cursive; font-weight: 400;
    font-size: 50px; color: var(--orchid); line-height: 1;
  }
  .portrait-ornament { position: absolute; left: 286px; top: 170px; width: 355px; height: 355px; background: var(--ornament); opacity: .35; border-radius: 6px; }
  .portrait {
    position: absolute; left: 313px; top: 196px; width: 301px; height: 301px;
    box-sizing: border-box; border: 6px solid var(--plum);
    background: linear-gradient(160deg, var(--photo-a), var(--photo-b));
  }
  .title {
    position: absolute; top: 548px; left: 0; width: 100%; margin: 0;
    text-align: center;
    font-family: "Yellowtail", cursive; font-weight: 400;
    font-size: 78px; color: var(--plum); line-height: 1;
  }
  .synopsis {
    position: absolute; top: 656px; left: 87px; width: 756px;
    font-family: "Mulish", sans-serif; font-weight: 700;
    font-size: 15.6px; line-height: 18.7px; letter-spacing: .25px;
    color: var(--plum);
  }
  .synopsis p { margin: 0 0 19px; }
  .site {
    position: absolute; top: 1106px; left: 0; width: 100%;
    text-align: center; margin: 0;
    font-family: "Mulish", sans-serif; font-weight: 800;
    font-size: 29px; color: var(--orchid);
  }
</style>
</head>
<body>
<main class="cover">
  <svg class="frame" width="927" height="1200" viewBox="0 0 927 1200" aria-hidden="true">
    <rect x="26" y="24" width="875" height="1152" fill="none" stroke="#6b449a" stroke-width="2"/>
  </svg>
  <div class="corner-ornament tl" role="img" aria-label="Ornamento de filigrana no canto superior esquerdo"></div>
  <div class="corner-ornament tr" role="img" aria-label="Ornamento de filigrana no canto superior direito"></div>
  <div class="corner-ornament bl" role="img" aria-label="Ornamento de filigrana no canto inferior esquerdo"></div>
  <div class="corner-ornament br" role="img" aria-label="Ornamento de filigrana no canto inferior direito"></div>

  <h2 class="author">Dra. Beatriz Morano Vasconti Telhado</h2>

  <div class="portrait-ornament" role="img" aria-label="Moldura ornamental em filigrana ao redor do retrato"></div>
  <div class="portrait" role="img" aria-label="Retrato da autora de jaleco branco sentada à mesa do consultório"></div>

  <h1 class="title">No Caminho do Amanhecer</h1>

  <section class="synopsis">
    <p>A busca pela fertilidade é um processo com várias etapas, desde a identificação do problema até sua resolução. A compreensão é essencial e ocorre logo depois ou concomitante à aceitação. Nesse momento o casal passa a entender a função existencial do ser humano. Ao definir suas prioridades o casal está apto à proceder com os passos seguintes. A fase da compreensão varia muito, podendo ser suficiente apenas uma conversa no consultório com um profissional, ou necessário a opinião de diversos profissionais; assim como também tem aqueles que precisam fazer uma ampla pesquisa na Internet, procuram entrevistas, vídeos e muito mais.</p>
    <p>O mundo globalizado de hoje oferece a possibilidade de diversas fontes de informação e isso é muito saudável. Entretanto, também se faz necessário uma fonte coerente, concisa, atualizada e confiável, exatamente o que este livro se propõe a fazer. Lembrando que o conhecimento do limite da ciência é muito importante para evitar abusos e sofrimentos desnecessários. Este livro almeja ser o guia ilustrado e explicado da fertilidade humana, respondendo o que, o como, o quando, o quem, o onde e o porque, de maneira compreensível e com o aprofundamento necessário para elucidar as dúvidas mais frequentes sobre esse assunto.</p>
    <p>A ciência tem que ser reconhecida pela sua transitoriedade que confere um caráter de mudanças contínuas, ou seja, o que é verdade hoje pode não ser amanhã. Mas, para aqueles que estão em busca de sua fertilidade, a verdade de hoje é a necessária, a de amanhã cabe aos especialistas. Apresentamos aqui a verdade atual sobre a fertilidade.</p>
  </section>

  <p class="site">www.ninhoclaro.org</p>
</main>
</body>
</html>
```